Business Card Design

Hoping for a black background business card, minimalistic design.
With the Marble Crest logo you created in white.

I would like to include:
My Name and title
Address (street address)
Reception: (phone number)
Fax: (fax number)
Reception: (email address)
Direct email: (email address)
Instagram: (ig handle)

```html
<!DOCTYPE html>
<html lang="en">
<head>
<meta charset="UTF-8">
<title>Marble Crest – Business Card</title>
<link href="https://fonts.googleapis.com/css2?family=Montserrat:wght@400;500;600;700&display=swap" rel="stylesheet">
<style>
  :root {
    --backdrop: #d9d9d9;
    --card-light: #f7f7f7;
    --card-dark: #050505;
    --ink-dark: #111111;
    --ink-light: #ffffff;
    --ink-muted: #cfcfcf;
    --ghost-on-light: #e4e4e4;
    --ghost-on-dark: #1b1b1b;
    --rule-dark: #8a8a8a;
  }
  * { box-sizing: border-box; margin: 0; padding: 0; }
  html, body { width: 1200px; height: 900px; overflow: hidden; }
  body {
    background: var(--backdrop);
    font-family: "Montserrat", sans-serif;
    display: flex;
    flex-direction: column;
    align-items: center;
    justify-content: center;
    gap: 50px;
  }
  .card {
    position: relative;
    width: 665px;
    height: 380px;
    overflow: hidden;
    box-shadow: 0 6px 18px rgba(0,0,0,0.18);
  }
  .card--front {
    background: var(--card-light);
    border-radius: 30px 4px 30px 4px;
  }
  .card--back {
    background: var(--card-dark);
    border-radius: 4px 40px 4px 30px;
    color: var(--ink-light);
  }
  .ghost-ring {
    position: absolute;
    border-radius: 50%;
    border: 14px solid;
  }
  .card--front .ghost-ring {
    width: 300px; height: 300px;
    right: -30px; top: -110px;
    border-color: var(--ghost-on-light);
  }
  .card--back .ghost-ring {
    width: 330px; height: 330px;
    left: 130px; top: 150px;
    border-color: var(--ghost-on-dark);
  }
  .lockup {
    position: absolute;
    display: flex;
    align-items: center;
    gap: 16px;
  }
  .lockup__dot {
    border-radius: 50%;
    border: 4px solid currentColor;
  }
  .lockup__divider {
    width: 1.5px;
    background: currentColor;
  }
  .lockup__name {
    font-weight: 500;
    letter-spacing: 0.08em;
    text-transform: uppercase;
    white-space: nowrap;
  }
  .card--front .lockup {
    left: 48px; bottom: 62px;
    color: var(--ink-dark);
  }
  .card--front .lockup__dot { width: 70px; height: 70px; }
  .card--front .lockup__divider { height: 86px; }
  .card--front .lockup__name { font-size: 36px; }

  .card--back .lockup {
    right: 46px; bottom: 40px;
    color: var(--ink-light);
  }
  .card--back .lockup__dot { width: 50px; height: 50px; border-width: 3px; }
  .card--back .lockup__divider { height: 62px; background: var(--rule-dark); }
  .card--back .lockup__name { font-size: 24px; }

  .holder {
    position: absolute;
    left: 46px; top: 150px;
  }
  .holder__name {
    font-weight: 700;
    font-size: 19px;
    letter-spacing: 0.04em;
    text-transform: uppercase;
    color: var(--ink-muted);
  }
  .holder__title {
    font-size: 14px;
    color: var(--ink-muted);
    margin-top: 4px;
  }
  .contact-line {
    display: flex;
    align-items: center;
    gap: 8px;
    font-size: 14.5px;
    color: var(--ink-light);
  }
  .holder .contact-line { margin-top: 8px; color: var(--ink-muted); }
  .contact-list {
    position: absolute;
    right: 46px; top: 58px;
    width: 330px;
    list-style: none;
    display: flex;
    flex-direction: column;
    gap: 6px;
    padding-bottom: 16px;
    border-bottom: 1px solid var(--rule-dark);
  }
  .icon { width: 15px; height: 15px; flex: none; fill: currentColor; }
  .icon--square {
    width: 14px; height: 14px;
    background: currentColor;
    border-radius: 3px;
    flex: none;
  }
</style>
</head>
<body>

  <section class="card card--front" aria-label="Card front">
    <div class="ghost-ring" aria-hidden="true"></div>
    <div class="lockup">
      <span class="lockup__dot" aria-hidden="true"></span>
      <span class="lockup__divider" aria-hidden="true"></span>
      <span class="lockup__name">Marble Crest</span>
    </div>
  </section>

  <section class="card card--back" aria-label="Card back">
    <div class="ghost-ring" aria-hidden="true"></div>

    <div class="holder">
      <p class="holder__name">Dana Whitfield</p>
      <p class="holder__title">Director</p>
      <p class="contact-line">
        <svg class="icon" viewBox="0 0 16 16" aria-hidden="true"><path d="M1 4h14v9H1z M1 4l7 5 7-5" fill="none" stroke="currentColor" stroke-width="1.6"/></svg>
        dana@marblecrest.co
      </p>
    </div>

    <ul class="contact-list">
      <li class="contact-line"><span class="icon--square" aria-hidden="true"></span>/marblecrest</li>
      <li class="contact-line">
        <svg class="icon" viewBox="0 0 16 16" aria-hidden="true"><path d="M4 1l3 3-2 2c1 2 3 4 5 5l2-2 3 3-2 3C7 14 2 9 1 3z"/></svg>
        555-210-4800
      </li>
      <li class="contact-line">
        <svg class="icon" viewBox="0 0 16 16" aria-hidden="true"><path d="M4 1h7v4H4z M1 6h14v8H1z" fill="none" stroke="currentColor" stroke-width="1.5"/></svg>
        555-310-4900
      </li>
      <li class="contact-line">
        <svg class="icon" viewBox="0 0 16 16" aria-hidden="true"><path d="M1 4h14v9H1z M1 4l7 5 7-5" fill="none" stroke="currentColor" stroke-width="1.6"/></svg>
        hello@marblecrest.co
      </li>
      <li class="contact-line">
        <svg class="icon" viewBox="0 0 16 16" aria-hidden="true"><path d="M8 1a5 5 0 0 1 5 5c0 4-5 9-5 9S3 10 3 6a5 5 0 0 1 5-5zm0 3a2 2 0 1 0 0 4 2 2 0 0 0 0-4z"/></svg>
        12 Harbor Lane, Westbury 4021
      </li>
    </ul>

    <div class="lockup">
      <span class="lockup__dot" aria-hidden="true"></span>
      <span class="lockup__divider" aria-hidden="true"></span>
      <span class="lockup__name">Marble Crest</span>
    </div>
  </section>

</body>
</html>
```